New Stationery New Logo for KT Fabrication Limited

We have a new logo and now want new stationary to go with it

This will be

Letterhead
Compliments Slip
Business Cards

Company details are
KT Fabrication Limited
Dellmoor Road, Rugby, Warwickshire, CV34 7HX, UK
Telephone : +44(0)1788 390617
Fax: +44(0)1788 473928
Email: sales@ktfabrication.co.uk
Web: www.ktfabrication.co.uk

Target Market(s)

Engineering / Metal Stamping

Industry/Entity Type

Manufacture

Contact Information for Business Card

Colin Brearley
Business Development Manager
KT Fabrication Limited
Dellmoor Road
Rugby
Warwickshire
CV34 7HX, UK

T: +44(0)1788 390617
F: +44(0)1788 473928
E: sales@ktfabrication.co.uk
W: www.ktfabrication.co.uk

Font styles to use
Sans Serif

Colors
33a6d7
0555a3
3176b5
85cae6
85acd3

Requirements
Must have
• Logo

```html
<!DOCTYPE html>
<html lang="en">
<head>
<meta charset="utf-8">
<title>KT Fabrication Stationery</title>
<link href="https://fonts.googleapis.com/css2?family=PT+Sans:wght@400;700&family=Pinyon+Script&display=swap" rel="stylesheet">
<style>
  :root{
    --backdrop:#a7a6a8;
    --paper:#f4f4f3;
    --navy:#0a3d8f;
    --brand:#0555a3;
    --ink:#3a3a3a;
    --ink-soft:#555;
    --black:#111;
  }
  *{margin:0;padding:0;box-sizing:border-box}
  html,body{width:1200px;height:770px;overflow:hidden}
  body{background:var(--backdrop);font-family:"PT Sans",sans-serif;color:var(--ink);position:relative}
  .sheet{position:absolute;background:var(--paper);box-shadow:0 2px 6px rgba(0,0,0,.25)}
  .accent-bar{position:absolute;width:6px;background:var(--brand)}
  .edge-bar{position:absolute;width:7px;background:var(--black)}
  .wordmark{display:flex;align-items:center;gap:6px;color:var(--brand);font-weight:400;letter-spacing:.28em;white-space:nowrap}
  .wordmark .dot{width:8px;height:8px;border-radius:50%;background:var(--brand);flex:none}
  .contacts{list-style:none}
  .contacts li{display:flex;align-items:center;gap:5px}
  .contacts svg{width:8px;height:8px;fill:var(--brand);flex:none}
  .company-name{font-weight:700}

  /* Letterhead */
  .letterhead{left:62px;top:33px;width:496px;height:702px}
  .letterhead .accent-bar{left:0;top:29px;height:86px}
  .letterhead .edge-bar{right:0;top:43px;height:60px}
  .letterhead .address{position:absolute;left:37px;top:37px;font-size:8.8px;line-height:11.5px}
  .letterhead .contacts{margin-top:5px;font-size:8.8px;line-height:12px}
  .letterhead .wordmark{position:absolute;right:42px;top:84px;font-size:10.5px}
  .letter{position:absolute;left:35px;top:222px;width:424px}
  .salutation{font-size:13px;color:var(--ink-soft);margin-bottom:30px}
  .letter p{font-size:7.3px;line-height:12px;text-align:justify;margin-bottom:12px;color:var(--ink)}
  .signoff{font-size:7.5px;margin-top:24px}
  .signature{width:66px;height:26px;margin:8px 0 0 14px;background:linear-gradient(90deg,rgba(30,30,30,.15),rgba(30,30,30,.05))}
  .signer{font-size:8.3px;line-height:13px;margin:10px 0 0 18px;color:var(--ink-soft)}

  /* Business card front */
  .card-front{left:623px;top:46px;width:218px;height:125px}
  .card-front .accent-bar{left:0;top:24px;width:5px;height:78px}
  .card-front .edge-bar{right:0;top:36px;width:5px;height:53px}
  .card-front .person{position:absolute;left:12px;top:21px}
  .card-front .person-name{font-size:8.3px;font-weight:700;color:var(--brand)}
  .card-front .person-role{font-size:5.6px;font-weight:700}
  .card-front .card-address{position:absolute;left:12px;top:44px;font-size:5.2px;line-height:6.5px}
  .card-front .contacts{margin-top:3px;font-size:5.2px;line-height:8.2px}
  .card-front .contacts svg{width:5px;height:5px}
  .card-front .wordmark{position:absolute;right:14px;top:75px;font-size:6.6px;gap:3px}
  .card-front .wordmark .dot{width:5px;height:5px}

  /* Business card back */
  .card-back{left:874px;top:46px;width:218px;height:125px;background:var(--navy)}
  .card-back .wordmark{position:absolute;left:0;right:0;top:55px;justify-content:center;color:#fff;font-size:10px}
  .card-back .wordmark .dot{background:#fff}
  .card-back .url{position:absolute;left:0;right:0;top:103px;text-align:center;color:#fff;font-size:6px;font-style:italic;letter-spacing:.2em}

  /* Compliments slip */
  .comp-slip{left:586px;top:194px;width:561px;height:254px}
  .comp-slip .accent-bar{left:0;top:21px;height:60px}
  .comp-slip .edge-bar{right:0;top:21px;width:6px;height:60px}
  .comp-slip .wordmark{position:absolute;left:24px;top:65px;font-size:10.5px}
  .comp-slip .address{position:absolute;right:142px;top:27px;text-align:right;font-size:8.8px;line-height:12px;border-right:1px solid #999;padding-right:6px}
  .comp-slip .contacts{position:absolute;left:427px;top:27px;font-size:8.8px;line-height:12px}
  .comp-slip .greeting{position:absolute;left:130px;top:135px;font-family:"Pinyon Script",cursive;font-size:44px;color:var(--navy)}

  /* Envelope */
  .envelope{left:586px;top:480px;width:561px;height:254px}
  .envelope .accent-bar{left:0;top:22px;height:92px}
  .envelope .wordmark{position:absolute;left:22px;top:63px;font-size:10.5px}
  .envelope .address{position:absolute;left:22px;top:82px;font-size:8.8px;line-height:11.5px}
</style>
</head>
<body>
<svg width="0" height="0" style="position:absolute" aria-hidden="true">
  <symbol id="icon-phone" viewBox="0 0 10 10"><path d="M2 0.5l2 2-1 1.3c.6 1.3 1.6 2.3 2.9 2.9l1.3-1 2 2-1.2 1.8C4.5 9.5.5 5.5.2 1.7z"/></symbol>
  <symbol id="icon-fax" viewBox="0 0 10 10"><rect x="2.5" y="0.5" width="5" height="3"/><rect x="0.5" y="4" width="9" height="4.5" rx=".8"/><rect x="2.5" y="7" width="5" height="2.5" fill="#fff"/></symbol>
  <symbol id="icon-mail" viewBox="0 0 10 10"><rect x="0.5" y="2" width="9" height="6.5"/><path d="M0.5 2L5 6 9.5 2" fill="none" stroke="#fff" stroke-width="1"/></symbol>
  <symbol id="icon-web" viewBox="0 0 10 10"><circle cx="5" cy="5" r="4.6"/><path d="M.5 5h9M5 .5c-2.4 2.8-2.4 6.2 0 9M5 .5c2.4 2.8 2.4 6.2 0 9" fill="none" stroke="#fff" stroke-width=".7"/></symbol>
</svg>

<section class="sheet letterhead">
  <div class="accent-bar"></div>
  <div class="edge-bar"></div>
  <div class="address">
    <div class="company-name">KT Fabrication Limited</div>
    <div>Dellmoor Road, Rugby</div>
    <div>Warwickshire, CV34 7HX, UK</div>
    <ul class="contacts">
      <li><svg><use href="#icon-phone"/></svg>+44(0)1788 390617</li>
      <li><svg><use href="#icon-fax"/></svg>+44(0)1788 473928</li>
      <li><svg><use href="#icon-mail"/></svg>sales@ktfabrication.co.uk</li>
      <li><svg><use href="#icon-web"/></svg>www.ktfabrication.co.uk</li>
    </ul>
  </div>
  <div class="wordmark"><span class="dot"></span>KT FABRICATION</div>
  <div class="letter">
    <div class="salutation">Dear Mr. Hartley,</div>
    <p>Lorem ipsum dolor sit amet, consectetur adipiscing elit. Donec orci purus, luctus vitae dignissim eu, iaculis sed purus. Vivamus faucibus, ipsum nec aliquet viverra, leo mauris condimentum ligula, sit amet sagittis enim ligula quis arcu. Nam egestas tortor id nisi porttitor mattis. In tortor ante, ultricies in suscipit a, tempus non massa. Vivamus et auctor mi. Fusce vel massa nulla. Phasellus nec eros mauris, et scelerisque orci.</p>
    <p>Donec malesuada orci vitae nulla accumsan porta a id massa. Quisque accumsan iaculis magna sit amet fringilla. Maecenas consequat, magna eget tincidunt semper, odio nibh rutrum mi, id feugiat ante nisi eu risus. Vestibulum nunc orci, rhoncus a placerat in, ultricies in mi. Cras mattis varius eros, vel fringilla nisi suscipit eget. Quisque scelerisque sagittis nulla at porttitor.</p>
    <p>Sed id augue vitae urna euismod commodo aliquet a quam. Pellentesque arcu velit, cursus et malesuada ut, consequat et diam. Nullam erat sem, rhoncus id ullamcorper vitae, rhoncus et arcu. In ultricies ultricies nulla, ut rutrum nisi iaculis at. Donec eu magna a metus ornare faucibus. Fusce aliquet faucibus ultricies. Morbi semper, est id tincidunt gravida, sem arcu adipiscing lacus, ac bibendum nulla leo eu purus. Quisque nec diam sed risus consectetur a cumsan quis quis nibh. Vestibulum id purus lorem.</p>
    <p>It is a long established fact that a reader will be distracted by the readable content of a page when looking at its layout. The point of using Lorem Ipsum is that it has a more-or-less normal distribution of letters, as opposed to using 'Content here, content here', making it look like readable English. Many desktop publishing packages</p>
    <div class="signoff">Sincerely,</div>
    <div class="signature" role="img" aria-label="Handwritten signature"></div>
    <div class="signer">Colin Brearley<br>CEO/ Founder</div>
  </div>
</section>

<section class="sheet card-front">
  <div class="accent-bar"></div>
  <div class="edge-bar"></div>
  <div class="person">
    <div class="person-name">Colin Brearley</div>
    <div class="person-role">CEO/Founder</div>
  </div>
  <div class="card-address">
    <div class="company-name">KT Fabrication Limited</div>
    <div>Dellmoor Road, Rugby,</div>
    <div>Warwickshire, CV34 7HX, UK</div>
    <ul class="contacts">
      <li><svg><use href="#icon-phone"/></svg>+44(0)1788 390617</li>
      <li><svg><use href="#icon-fax"/></svg>+44(0)1788 473928</li>
      <li><svg><use href="#icon-mail"/></svg>sales@ktfabrication.co.uk</li>
      <li><svg><use href="#icon-web"/></svg>www.ktfabrication.co.uk</li>
    </ul>
  </div>
  <div class="wordmark"><span class="dot"></span>KT FABRICATION</div>
</section>

<section class="sheet card-back">
  <div class="wordmark"><span class="dot"></span>KT FABRICATION</div>
  <div class="url">www.ktfabrication.co.uk</div>
</section>

<section class="sheet comp-slip">
  <div class="accent-bar"></div>
  <div class="edge-bar"></div>
  <div class="wordmark"><span class="dot"></span>KT FABRICATION</div>
  <div class="address">
    <div class="company-name">KT Fabrication Limited</div>
    <div>Dellmoor Road, Rugby</div>
    <div>Warwickshire</div>
    <div>CV34 7HX, UK</div>
  </div>
  <ul class="contacts">
    <li><svg><use href="#icon-phone"/></svg>+44(0)1788 390617</li>
    <li><svg><use href="#icon-fax"/></svg>+44(0)1788 473928</li>
    <li><svg><use href="#icon-mail"/></svg>sales@ktfabrication.co.uk</li>
    <li><svg><use href="#icon-web"/></svg>www.ktfabrication.co.uk</li>
  </ul>
  <div class="greeting">With Compliments</div>
</section>

<section class="sheet envelope">
  <div class="accent-bar"></div>
  <div class="wordmark"><span class="dot"></span>KT FABRICATION</div>
  <div class="address">
    <div class="company-name">KT Fabrication Limited</div>
    <div>Dellmoor Road, Rugby</div>
    <div>Warwickshire, CV34 7HX, UK</div>
  </div>
</section>
</body>
</html>
```